Luxury Lifestyle Website - Blog and Product Showcasing

I am looking to create a simple, yet elegant website where I can post blog posts and feature products and brand partnerships for my company, Velour Hollis. I want a very elegant but not overly complex site. I like the look and feel of Harriet Osborne's site - I don't need for it to be that robust or sophisticated, but that is the aesthetic I am going for. I would like to include my primary logo at the top of the main page, and also incorporate my alternative logos throughout the site in strategic places.

Target Market(s)

Luxury Brands; 20s-60s year olds; women; high-end fashion and tastes

Industry/Entity Type

Luxury Lifestyle - Blogging - Product Showcasing

Coding

Coded - Design and coding required

Number of Pages Required

4 page

Font styles to use
Sans Serif
Script
Other font styles liked:
• Pinyon

Colors
00AB8E
00BBA5
67D7C9
C6EFE9
E9F9F6
59FF00
82FF00
B8FF75
E3FFCB
F4FFEA

Requirements
Must have
• Creative use of my various logos. PASTEL GREENS or a DEEP DARK GREEN. Nothing bright, very soft and elegant.
Nice to have
• Elegant script that is easy to read.
Should not have
• Bright colors or overly modern look or feel.

```html
<!DOCTYPE html>
<html lang="en">
<head>
<meta charset="utf-8">
<title>Velour Hollis — Luxury Lifestyle</title>
<link href="https://fonts.googleapis.com/css2?family=Literata:ital,opsz,wght@0,7..72,400;0,7..72,500;0,7..72,700;1,7..72,400&family=Jost:wght@400&display=swap" rel="stylesheet">
<style>
:root{
  --ink:#111111;
  --text:#555555;
  --paper:#ffffff;
  --mint:#e3fccb;
  --hero-a:#d8dcc6;
  --hero-b:#e6ebd2;
  --line:#8a8a8a;
  --photo-warm:#c9b59a;
  --photo-cool:#9aa6a0;
  --photo-dark:#3b3f3d;
}
*{box-sizing:border-box;margin:0;padding:0}
html,body{width:1200px;height:3939px;overflow:hidden}
body{position:relative;background:var(--paper);font-family:"Literata",Georgia,serif;color:var(--ink)}
.abs{position:absolute}
a{color:var(--ink)}
.btn{position:absolute;display:flex;align-items:center;justify-content:center;border:1px solid var(--ink);font-size:17px;color:var(--ink);text-decoration:none;background:transparent}
.photo{position:absolute}

/* header */
.site-header{position:absolute;left:0;top:0;width:1200px;height:102px}
.menu-icon{left:89px;top:37px}
.nav-item{position:absolute;top:33px;font-size:18px}
.brand-name{position:absolute;font-family:"Literata",Georgia,serif;font-weight:400;color:var(--ink);white-space:nowrap}
.header-brand{left:0;width:1200px;top:22px;text-align:center;font-size:34px}

/* hero */
.hero{left:0;top:102px;width:1200px;height:546px;background:linear-gradient(135deg,var(--hero-a),var(--hero-b) 55%,#dfe4cc)}
.hero-title{position:absolute;left:0;width:1200px;top:236px;text-align:center;font-weight:700;font-size:62px;line-height:88px}

/* partners */
.partner{position:absolute;top:705px;font-size:26px;color:var(--ink);white-space:nowrap;text-align:center}

/* featured */
.section-title{position:absolute;font-size:37px;font-weight:400}
.card-label{position:absolute;font-size:21px;text-align:center;width:328px}
.see-all{position:absolute;font-size:17px;text-align:center;width:328px}

/* about */
.about-title{left:702px;top:1733px;font-style:italic;font-size:37px}
.body-copy{position:absolute;font-size:16px;line-height:27.5px;color:var(--text)}

/* partnership */
.partner-band{left:0;top:2246px;width:1200px;height:506px;background:var(--mint)}

/* blog */
.blog-rule{position:absolute;height:1px;width:245px;background:var(--line)}
.blog-title{position:absolute;width:245px;text-align:center;font-size:22px;font-weight:500}

/* footer */
.site-footer{left:0;top:3643px;width:1200px;height:296px;background:var(--mint)}
.footer-heading{position:absolute;font-size:21px;font-weight:500}
.footer-link{position:absolute;left:523px;font-size:16px;color:var(--text)}
.email-field{position:absolute;left:723px;top:3793px;width:388px;height:58px;border:1px solid var(--ink);background:var(--paper);font-size:12px;color:var(--text);padding:20px 0 0 28px}
.subscribe{position:absolute;left:992px;top:3793px;width:119px;height:58px;background:var(--ink);color:#fff;font-size:15px;display:flex;align-items:center;justify-content:center;text-decoration:underline}
.legal{position:absolute;top:3910px;font-size:12px;color:var(--ink)}
</style>
</head>
<body>

<header class="site-header">
  <svg class="abs menu-icon" width="34" height="18" viewBox="0 0 34 18"><path d="M0 1H34M0 9H34M0 17H34" stroke="#111" stroke-width="1.4"/></svg>
  <span class="nav-item" style="left:174px">Menu</span>
  <span class="brand-name header-brand">Velour Hollis</span>
  <span class="nav-item" style="left:960px">Search</span>
  <span class="nav-item" style="left:1067px">Shop</span>
</header>

<section class="abs hero" role="img" aria-label="Woman carrying luxury shopping bags on a city street, pale green tint"></section>
<h1 class="hero-title">Welcome To Velour Hollis<br>Luxury Style</h1>
<a class="btn" style="left:477px;top:469px;width:245px;height:57px">Shop Now</a>

<div class="partner" style="left:110px;width:220px;letter-spacing:14px;font-family:'Jost',sans-serif">MAREN</div>
<div class="partner" style="left:420px;width:115px">Ostrava</div>
<div class="partner" style="left:612px;width:170px">Atelier Row</div>
<div class="partner" style="left:875px;width:220px">Lucien Varro</div>

<h2 class="section-title" style="left:89px;top:862px">Featured Post</h2>
<a class="btn" style="left:867px;top:853px;width:244px;height:57px">View All Post</a>

<div class="photo" style="left:89px;top:939px;width:328px;height:402px;background:linear-gradient(160deg,#ece6dc,var(--photo-warm))" role="img" aria-label="Tan leather handbag carried over a pleated dress"></div>
<div class="card-label" style="left:89px;top:1358px">Hand Bags</div>
<a class="see-all" style="left:89px;top:1402px">See All</a>

<div class="photo" style="left:436px;top:940px;width:328px;height:466px;background:linear-gradient(180deg,#4e6a8c 0%,#8e9cb0 30%,#d8c1a0 60%,#9e9e9a)" role="img" aria-label="Nude strappy block-heel sandals with cropped jeans"></div>
<div class="card-label" style="left:436px;top:1426px">Shoes</div>
<a class="see-all" style="left:436px;top:1469px">See All</a>

<div class="photo" style="left:783px;top:940px;width:328px;height:555px;background:linear-gradient(170deg,#e4e2e0,#c7b39a 60%,#6d6660)" role="img" aria-label="Woman in a beige dress seated in front of the Eiffel Tower"></div>
<div class="card-label" style="left:783px;top:1514px">Dress</div>
<a class="see-all" style="left:783px;top:1558px">See All</a>

<div class="photo" style="left:0;top:1616px;width:364px;height:244px;background:linear-gradient(120deg,#1f4a45,#5d6a66 50%,#cfc6b6)" role="img" aria-label="Woman in a trench coat and red boots crossing a street"></div>
<div class="photo" style="left:373px;top:1697px;width:304px;height:362px;background:linear-gradient(90deg,#b8b0a6,#1e3b36 45%,#3a4a44)" role="img" aria-label="Woman in a grey coat walking past a dark green door"></div>
<div class="photo" style="left:180px;top:1769px;width:306px;height:325px;background:#fff;padding:8px">
  <div style="width:100%;height:100%;background:linear-gradient(150deg,#d9cbb5,#9a8a76 55%,#3d3835)" role="img" aria-label="Woman in a camel jacket and black boots seated on stone steps"></div>
</div>
<h2 class="section-title about-title">About Velour Hollis</h2>
<p class="body-copy" style="left:702px;top:1788px;width:410px">Lorem ipsum dolor sit amet, consectetur adipiscing elit, sed do eiusmod tempor incididunt ut labore et dolore magna aliqua. Ut enim ad minim veniam, quis nostrud exercitation ullamco laboris nisi ut aliquip ex ea commodo consequat. Duis aute irure dolor in reprehenderit in voluptate velit esse cillum dolore eu fugiat nulla pariatur. Excepteur sint occaecat cupidatat non proident, sunt in culpa qui officia deserunt mollit anim id est laborum.</p>

<section class="abs partner-band"></section>
<div class="photo" style="left:679px;top:2198px;width:431px;height:554px;background:linear-gradient(160deg,#d6d9dc,#8a8d90 45%,#1c1c1e);box-shadow:0 6px 18px rgba(0,0,0,.18)" role="img" aria-label="Woman in a knit beanie and sunglasses holding a black leather handbag"></div>
<h2 class="section-title" style="left:87px;top:2364px">Brand Partnership</h2>
<p class="body-copy" style="left:87px;top:2421px;width:575px">Lorem ipsum dolor sit amet, consectetur adipiscing elit, sed do eiusmod tempor incididunt ut labore et dolore magna aliqua. Ut enim ad minim veniam, quis nostrud exercitation ullamco laboris nisi ut aliquip ex ea commodo consequat. Duis aute irure dolor in reprehenderit in voluptate velit esse cillum dolore eu fugiat nulla pariatur. Excepteur sint occaecat cupidatat non proident, sunt in culpa qui officia deserunt mollit anim id est laborum.</p>

<h2 class="section-title" style="left:0;width:1200px;text-align:center;top:2850px">Blog Post</h2>

<div class="photo" style="left:182px;top:2915px;width:241px;height:373px;background:linear-gradient(170deg,#ece9e4,#b48a62 45%,#efece8)" role="img" aria-label="Woman with curly hair wearing sunglasses"></div>
<div class="blog-rule" style="left:182px;top:3320px"></div>
<div class="blog-title" style="left:182px;top:3327px">Blog Title</div>
<div class="blog-rule" style="left:182px;top:3362px"></div>
<p class="body-copy" style="left:182px;top:3377px;width:250px">Lorem ipsum dolor sit amet, consectetur adipiscing elit, sed do eiusmod tempor incididunt ut labore et dolore magna aliqua.</p>

<div class="photo" style="left:477px;top:2915px;width:241px;height:373px;background:linear-gradient(160deg,#2b2b2d,#777 45%,#e8e4dc 60%,#3a3a3c)" role="img" aria-label="Cream wedge slide sandals on a dark floor"></div>
<div class="blog-rule" style="left:477px;top:3320px"></div>
<div class="blog-title" style="left:477px;top:3327px">Blog Title</div>
<div class="blog-rule" style="left:477px;top:3362px"></div>
<p class="body-copy" style="left:477px;top:3377px;width:250px">Lorem ipsum dolor sit amet, consectetur adipiscing elit, sed do eiusmod tempor incididunt ut labore et dolore magna aliqua.</p>

<div class="photo" style="left:772px;top:2915px;width:241px;height:373px;background:linear-gradient(170deg,#111,#555 45%,#9a9a9a 70%,#2a2a2a)" role="img" aria-label="Hand with a silver watch holding a crystal-embellished clutch"></div>
<div class="blog-rule" style="left:772px;top:3320px"></div>
<div class="blog-title" style="left:772px;top:3327px">Blog Title</div>
<div class="blog-rule" style="left:772px;top:3362px"></div>
<p class="body-copy" style="left:772px;top:3377px;width:250px">Lorem ipsum dolor sit amet, consectetur adipiscing elit, sed do eiusmod tempor incididunt ut labore et dolore magna aliqua.</p>

<a class="btn" style="left:477px;top:3524px;width:245px;height:58px;text-decoration:underline">View All Blogs</a>

<footer class="abs site-footer"></footer>
<span class="brand-name" style="left:93px;top:3690px;font-size:38px">Velour Hollis</span>
<p class="body-copy" style="left:90px;top:3777px;width:330px;color:var(--ink)">Lorem ipsum dolor sit amet, consectetur adipiscing elit, sed do eiusmod tempor incididunt ut labore et dolore magna aliqua.</p>
<div class="footer-heading" style="left:523px;top:3698px">Quick Link</div>
<a class="footer-link" style="top:3754px">About</a>
<a class="footer-link" style="top:3785px">Product</a>
<a class="footer-link" style="top:3815px">Shop</a>
<a class="footer-link" style="top:3846px">Search</a>
<div class="footer-heading" style="left:723px;top:3698px">Newsletter</div>
<p class="body-copy" style="left:723px;top:3750px;width:400px">Lorem ipsum dolor sit amet, consectetur adipiscing,</p>
<div class="email-field">Enter your email address</div>
<a class="subscribe">Subscribe</a>
<div class="abs" style="left:0;top:3900px;width:1200px;height:1px;background:var(--ink)"></div>
<span class="legal" style="left:89px">© 2023 VelourHollis.All rights reserved</span>
<span class="legal" style="left:857px">Teerms &amp; Conditions</span>
<span class="legal" style="left:1017px">Privacy &amp; Policy</span>

</body>
</html>
```